Washing Up Liquid Label

We are looking for 2 labels to be designed to be part of a range of products.

The brand is Velmora Max and we are looking for a label design to you on washing up liquid bottle similar to the ones in the file attached.

One label it be original and the liquid will be green so the label colour needs to be green or work with the green. The other label is lemon and is yellow.

Please see attached the Velmora Max logo and also a couple of the other designs in the range.

```html
<!DOCTYPE html>
<html lang="en">
<head>
<meta charset="utf-8">
<title>Velmora Max – Lemon Washing Up Liquid Label</title>
<link rel="stylesheet" href="https://fonts.googleapis.com/css2?family=Arimo:wght@700&family=Tinos:ital@0;1&display=swap">
<style>
  :root {
    --paper: #ffffff;
    --lemon-deep: #f2e600;
    --lemon-mid: #f5ec45;
    --lemon-soft: #f8f17c;
    --lemon-light: #fbf6b4;
    --lemon-pale: #fdfbe0;
    --brand-blue: #1d5fb4;
    --accent-red: #e3071b;
    --leaf-green: #2fa345;
    --fruit-yellow: #f6c21c;
    --fruit-light: #fbe38a;
  }
  html, body {
    margin: 0;
    padding: 0;
    width: 1200px;
    height: 1000px;
    overflow: hidden;
    background: var(--paper);
  }
  .canvas {
    position: relative;
    width: 1200px;
    height: 1000px;
    background: var(--paper);
  }
  .label-ring {
    position: absolute;
    left: 0;
    top: 0;
  }
  .label-text {
    position: absolute;
    left: 300px;
    width: 610px;
    margin: 0;
    text-align: center;
    line-height: 1;
    white-space: nowrap;
  }
  .brand-name {
    top: 336px;
    font-family: "Arimo", Arial, sans-serif;
    font-weight: 700;
    font-size: 78px;
    color: var(--brand-blue);
  }
  .tagline {
    top: 486px;
    font-family: "Arimo", Arial, sans-serif;
    font-weight: 700;
    font-size: 52px;
    color: var(--accent-red);
  }
  .subline {
    top: 542px;
    font-family: "Tinos", "Times New Roman", serif;
    font-size: 31px;
    color: var(--leaf-green);
  }
  .fragrance-art {
    position: absolute;
    left: 382px;
    top: 600px;
    width: 452px;
    height: 136px;
    border-radius: 68px;
    background: radial-gradient(ellipse at 50% 50%, var(--fruit-yellow) 0%, #f8cf45 35%, var(--fruit-light) 75%, #fdf1c2 100%);
  }
  .fragrance-name {
    top: 741px;
    font-family: "Tinos", "Times New Roman", serif;
    font-style: italic;
    font-size: 31px;
    color: var(--accent-red);
  }
</style>
</head>
<body>
  <main class="canvas">
    <svg class="label-ring" width="1200" height="1000" viewBox="0 0 1200 1000" aria-hidden="true">
      <defs>
        <radialGradient id="innerGlow" cx="0.5" cy="0.45" r="0.55">
          <stop offset="0.8" stop-color="#ffffff"/>
          <stop offset="1" stop-color="#fdfbe0"/>
        </radialGradient>
      </defs>
      <ellipse class="ring-band" cx="603" cy="488" rx="305" ry="320" fill="var(--lemon-deep)"/>
      <ellipse class="ring-band" cx="603" cy="481" rx="296" ry="311" fill="var(--lemon-mid)"/>
      <ellipse class="ring-band" cx="603" cy="474" rx="288" ry="302" fill="var(--lemon-soft)"/>
      <ellipse class="ring-band" cx="602" cy="467" rx="280" ry="294" fill="var(--lemon-light)"/>
      <ellipse class="ring-band" cx="602" cy="460" rx="272" ry="286" fill="var(--lemon-pale)"/>
      <ellipse class="ring-centre" cx="601" cy="452" rx="264" ry="278" fill="url(#innerGlow)"/>
    </svg>

    <h1 class="label-text brand-name">Velmora Max</h1>
    <p class="label-text tagline">clean &amp; fresh</p>
    <p class="label-text subline">For Cleaner Dishes</p>
    <div class="fragrance-art" role="img" aria-label="Halved lemon with green leaves flanked by white daisies"></div>
    <p class="label-text fragrance-name">lemon</p>
  </main>
</body>
</html>
```